RESIDENTIAL CONSTRUCTION

We are a company that specializes in building custom residential homes, the design should also emphasize that quality and service is our priority.

Industry/Entity Type

Construction Company

Contact Information for Business Card

Contact Person: Tobias Lindqvar
Company Address: 463 Westbrook Ave San Jose , Ca 95112
Phone Number : 408-731-2946
Email Address: Oakfieldcrafters731@mailvessel.net

Font styles to use
Sans Serif

Colors
ec1f27

Requirements
Must have
• CSLB # 7362519
Nice to have
• needs to have same color as logo i uploaded, we will be printing these on a clear plastic card.

```html
<!DOCTYPE html>
<html lang="en">
<head>
<meta charset="utf-8">
<title>Oakfield Crafters — Business Card</title>
<link href="https://fonts.googleapis.com/css2?family=Roboto:wght@400;500;700&display=swap" rel="stylesheet">
<style>
  :root {
    --brand-red: #be1e2d;
    --ink: #111111;
    --paper: #ffffff;
    --backdrop: #f1f1f1;
    --card-shadow: rgba(0, 0, 0, 0.16);
  }
  * { margin: 0; padding: 0; box-sizing: border-box; }
  html, body {
    width: 1200px;
    height: 1200px;
    overflow: hidden;
    background: var(--backdrop);
    font-family: "Roboto", Arial, sans-serif;
  }
  .canvas {
    position: relative;
    width: 1200px;
    height: 1200px;
  }
  .card {
    position: absolute;
    left: 180px;
    width: 840px;
    height: 480px;
    background: var(--paper);
    box-shadow: 0 6px 22px var(--card-shadow);
    overflow: hidden;
  }
  .card--front { top: 90px; }
  .card--back { top: 630px; }

  .card__shapes {
    position: absolute;
    inset: 0;
    width: 840px;
    height: 480px;
  }
  .contact-name {
    position: absolute;
    left: 48px;
    top: 86px;
    color: var(--paper);
    font-weight: 700;
    font-size: 25px;
    letter-spacing: 0.5px;
    text-transform: uppercase;
  }
  .contact-line {
    position: absolute;
    left: 48px;
    color: var(--paper);
    font-size: 16px;
    font-weight: 400;
    white-space: nowrap;
  }
  .contact-line--phone { top: 218px; }
  .contact-line--email { top: 284px; }
  .contact-line--address { top: 350px; }

  .brand {
    position: absolute;
    display: flex;
    align-items: center;
    gap: 12px;
    color: var(--brand-red);
    font-weight: 700;
    text-transform: uppercase;
    white-space: nowrap;
  }
  .brand__mark {
    background: var(--brand-red);
    flex: none;
  }
  .brand--small {
    left: 470px;
    top: 150px;
    font-size: 26px;
    letter-spacing: 0.3px;
    gap: 10px;
  }
  .brand--small .brand__mark { width: 22px; height: 22px; }
  .brand--large {
    left: 50%;
    top: 50%;
    transform: translate(-50%, -50%);
    font-size: 56px;
    letter-spacing: 1px;
    gap: 20px;
  }
  .brand--large .brand__mark { width: 48px; height: 48px; }

  .license {
    position: absolute;
    left: 640px;
    top: 292px;
    color: var(--ink);
    font-size: 15px;
    font-weight: 500;
  }
</style>
</head>
<body>
<main class="canvas">

  <section class="card card--front" aria-label="Business card front">
    <svg class="card__shapes" viewBox="0 0 840 480" aria-hidden="true">
      <polygon points="0,0 300,0 620,480 0,480" fill="var(--brand-red)"/>
      <polygon points="380,196 431,196 474,260 380,260" fill="var(--ink)"/>
      <polygon points="424,262 475,262 518,326 424,326" fill="var(--ink)"/>
      <polygon points="468,328 519,328 562,392 468,392" fill="var(--ink)"/>
      <line x1="48" y1="261" x2="424" y2="261" stroke="var(--paper)" stroke-width="2"/>
      <line x1="48" y1="327" x2="468" y2="327" stroke="var(--paper)" stroke-width="2"/>
      <g fill="var(--paper)" transform="translate(400,214)">
        <rect x="2" y="10" width="26" height="16" rx="3"/>
        <path d="M0 9 Q15 -2 30 9 L27 13 Q15 5 3 13 Z"/>
      </g>
      <g transform="translate(444,282)">
        <rect x="0" y="0" width="30" height="22" fill="var(--paper)"/>
        <polyline points="0,0 15,12 30,0" fill="none" stroke="var(--ink)" stroke-width="2"/>
      </g>
      <g transform="translate(492,342)">
        <path d="M12 0 A9 9 0 0 1 21 9 C21 16 12 26 12 26 C12 26 3 16 3 9 A9 9 0 0 1 12 0 Z" fill="var(--paper)"/>
        <circle cx="12" cy="9" r="3.5" fill="var(--ink)"/>
        <rect x="0" y="27" width="24" height="4" fill="var(--paper)"/>
      </g>
    </svg>

    <h1 class="contact-name">Tobias Lindqvar</h1>
    <p class="contact-line contact-line--phone">408-731-2946</p>
    <p class="contact-line contact-line--email">Oakfieldcrafters731@mailvessel.net</p>
    <p class="contact-line contact-line--address">463 Westbrook Ave San Jose , Ca 95112</p>

    <div class="brand brand--small">
      <span class="brand__mark"></span>
      <span class="brand__name">Oakfield Crafters</span>
    </div>
    <p class="license">CSLB # 7362519</p>
  </section>

  <section class="card card--back" aria-label="Business card back">
    <div class="brand brand--large">
      <span class="brand__mark"></span>
      <span class="brand__name">Oakfield Crafters</span>
    </div>
  </section>

</main>
</body>
</html>
```